Resposive web site in 4 languages + image gallery + logo design

We need a web page, which will work on all devices.
I have uploaded web page concept.
Company name: Quarnela
Industry/Entity Type
It Company
Logo Text
quality matters
Coding
Coded - Design and coding required
Number of Pages Required
1 page

```html
<!DOCTYPE html>
<html lang="en">
<head>
<meta charset="utf-8">
<title>Quarnela – Quality Handmade Product</title>
<link rel="stylesheet" href="https://fonts.googleapis.com/css2?family=Lora:wght@400;700&family=Roboto:wght@400;500;700&display=swap">
<style>
:root{
  --gold:#a8792a;
  --gold-dark:#8e6420;
  --gold-light:#c9a25a;
  --ink:#2b2b2b;
  --muted:#6d6d6d;
  --band:#eeeeee;
  --services-bg:#3a332c;
  --panel:#f3ead8;
  --panel-alt:#e4e1dc;
  --contact-bg:#cdb68d;
  --field:#c4a977;
  --footer:#222222;
  --white:#ffffff;
}
*{box-sizing:border-box;margin:0;padding:0}
html,body{width:1200px;height:2620px;overflow:hidden}
body{position:relative;background:var(--white);font-family:'Roboto',Arial,sans-serif;color:var(--ink)}
.abs{position:absolute}
.serif{font-family:'Lora',Georgia,serif}

/* hero */
.hero{left:0;top:0;width:1200px;height:580px;background:linear-gradient(90deg,#4a2a22 0%,#7a4a33 35%,#a3714a 55%,#6b3f2c 80%,#2f2018 100%)}
.topbar{left:0;top:0;width:1200px;height:91px;background:rgba(20,12,8,.55)}
.logo-box{border:2px solid #777;background:#9a9696;overflow:hidden}
.logo-box svg{position:absolute;left:0;top:0;width:100%;height:100%}
.logo-box span{position:absolute;left:0;right:0;bottom:10%;text-align:center;font-family:'Roboto',Arial,sans-serif;color:#222}
.contact-line{left:727px;top:14px;font-size:12px;color:var(--white);font-weight:500;display:flex;gap:22px;align-items:center}
.social{display:flex;gap:10px;font-size:11px}
.nav{left:728px;top:50px;display:flex;gap:26px;font-size:11px;font-weight:700;color:var(--white);text-transform:uppercase}
.nav .active{border-bottom:1px solid var(--white);padding-bottom:6px}
.hero-title{left:353px;top:257px;width:493px;height:66px;background:rgba(60,30,20,.45);color:var(--white);font-size:33px;font-style:italic;text-align:center;line-height:66px}

/* feature cards */
.card-img{width:269px;height:151px;border:3px solid var(--white);box-shadow:0 1px 4px rgba(0,0,0,.25)}
.card-title{font-size:21px;color:var(--gold)}
.card-text{font-size:11px;line-height:18px;color:#555;width:270px}

/* estimate band */
.estimate{left:0;top:797px;width:1200px;height:73px;background:var(--band)}
.estimate h2{left:178px;top:18px;font-size:26px;font-weight:400;color:#222}
.btn{background:var(--gold);color:var(--white);text-align:center;font-family:'Lora',Georgia,serif}
.btn-quote{left:793px;top:15px;width:201px;height:39px;line-height:39px;font-size:20px;border:2px solid var(--gold-dark)}

/* services */
.services{left:0;top:870px;width:1200px;height:886px;background:linear-gradient(180deg,#3f372f,#2e2822)}
.section-title{font-size:28px;color:var(--gold-light);display:flex;align-items:center;gap:16px;justify-content:center;width:1200px;left:0}
.section-title::before,.section-title::after{content:"";width:54px;height:5px;border-top:1px solid currentColor;border-bottom:1px solid currentColor}
.service{left:161px;width:879px;height:241px;background:var(--panel)}
.service.alt{background:var(--panel-alt)}
.service-img{width:267px;height:194px;border:3px solid var(--white)}
.service-img .caption{position:absolute;left:0;bottom:10px;background:var(--gold);color:var(--white);font-family:'Lora',Georgia,serif;font-size:13px;padding:4px 18px}
.service-img .arrow{position:absolute;top:86px;color:#222;font-size:16px}
.service h3{font-size:19px;font-weight:400;color:#222;border-bottom:1px solid #333;padding-bottom:3px}
.service p{font-size:11px;line-height:22px;color:#8a8a8a;width:545px}
.read-more{font-size:12px;color:var(--gold)}

/* about */
.about-title{top:1782px;color:var(--gold)}
.about-text{left:404px;top:1845px;width:620px;font-size:11px;line-height:17px;color:#444}
.about-text p{margin-bottom:16px}

/* contact */
.contact-photo{left:0;top:2000px;width:611px;height:369px;background:linear-gradient(120deg,#8b7a63 0%,#d7c09b 45%,#b68c5e 75%,#e8dcc4 100%)}
.contact-panel{left:611px;top:2000px;width:589px;height:369px;background:var(--contact-bg)}
.contact-head{left:613px;top:2039px;width:418px;height:57px;background:var(--gold);color:var(--white);font-family:'Lora',Georgia,serif;font-weight:700;font-size:15px;line-height:20px;text-align:center;padding-top:8px}
.field{background:var(--field);border:1px solid #a3834d;color:var(--white);font-size:14px;padding:7px 12px}
.btn-send{left:758px;top:2313px;width:126px;height:31px;line-height:31px;font-size:16px}

/* footer */
.footer{left:0;top:2369px;width:1200px;height:251px;background:var(--footer);color:var(--white)}
.footer-info{font-size:13px;line-height:19px}
.links{font-size:11px;line-height:26px;list-style:none}
.newsletter-title{font-size:20px}
.news-input{left:760px;top:98px;width:264px;height:26px;background:var(--white);color:#999;font-size:11px;font-style:italic;padding:6px 10px}
.btn-submit{left:760px;top:133px;width:84px;height:23px;line-height:23px;font-family:'Roboto',Arial,sans-serif;font-size:11px;font-weight:700}
.copyright{left:180px;top:220px;font-size:11px}
.to-top{left:988px;top:215px;width:34px;height:34px;border:1px solid var(--white);border-radius:50%}
</style>
</head>
<body>

<header>
  <div class="abs hero" role="img" aria-label="Photo of a warm vintage living room with gramophone, armchairs and bookshelves"></div>
  <div class="abs topbar"></div>
  <div class="abs logo-box" style="left:175px;top:17px;width:192px;height:109px">
    <svg viewBox="0 0 192 109" preserveAspectRatio="none"><line x1="0" y1="0" x2="192" y2="109" stroke="#555" stroke-width="1"/><line x1="192" y1="0" x2="0" y2="109" stroke="#555" stroke-width="1"/></svg>
    <span style="font-size:18px;bottom:18px">Quarnela</span>
  </div>
  <div class="abs contact-line">
    <span>Call Us. +372 55 01234</span>
    <span>Language <svg width="14" height="9" viewBox="0 0 14 9"><rect width="14" height="9" fill="#2a3f8f"/><path d="M0 4.5h14M7 0v9" stroke="#fff" stroke-width="2"/><path d="M0 4.5h14M7 0v9" stroke="#c8102e" stroke-width="1"/></svg> ˅</span>
    <span class="social"><span>f</span><span>t</span></span>
  </div>
  <nav class="abs nav">
    <span class="active">Home</span><span>Services</span><span>About us</span><span>Contact us</span>
  </nav>
  <h1 class="abs hero-title serif" style="font-weight:400">Quality Handmade Product</h1>
</header>

<section class="features">
  <div class="abs card-img" style="left:171px;top:501px;background:linear-gradient(135deg,#c8a983,#7b5a3e)" role="img" aria-label="Photo of a carved wooden interior with stacked firewood"></div>
  <div class="abs card-img" style="left:466px;top:501px;background:linear-gradient(135deg,#b9b6ae,#6f6a61)" role="img" aria-label="Photo of a stone archway entrance with wooden door"></div>
  <div class="abs card-img" style="left:762px;top:501px;background:linear-gradient(135deg,#d19a5e,#8c5a2e)" role="img" aria-label="Photo of craftsmen restoring a wooden floor"></div>

  <h3 class="abs card-title serif" style="left:178px;top:660px;font-weight:400">Wood Works</h3>
  <p class="abs card-text" style="left:177px;top:702px">Wood is also relatively durable and easy to work with, which has made it a favourite of builders throughout history.</p>
  <h3 class="abs card-title serif" style="left:473px;top:660px;font-weight:400">Stone Works</h3>
  <p class="abs card-text" style="left:473px;top:702px">The natural stone found in the ground has been used in construction for centuries because of its durability.</p>
  <h3 class="abs card-title serif" style="left:766px;top:660px;font-weight:400">Restoration</h3>
  <p class="abs card-text" style="left:766px;top:702px">The extensive experience of our craftsmen will help you achieve the desired result of restoring valuable old windows and pieces of furniture.</p>
</section>

<section class="abs estimate">
  <h2 class="abs serif">Are you interested in an estimate?</h2>
  <div class="abs btn btn-quote">GET A QUOTE</div>
</section>

<section class="abs services" role="img" aria-label="Dimmed photo of a lounge with leather armchairs"></section>
<h2 class="abs section-title serif" style="top:895px;font-weight:400">Our Services</h2>

<article class="abs service" style="top:957px">
  <div class="abs service-img" style="left:21px;top:23px;background:linear-gradient(135deg,#b89572,#5e4531)" role="img" aria-label="Photo of a curved wooden staircase">
    <span class="arrow" style="left:4px">‹</span><span class="arrow" style="right:4px">›</span>
    <span class="caption">Wooden Staircases</span>
  </div>
  <h3 class="abs serif" style="left:315px;top:22px">Wood Works</h3>
  <p class="abs" style="left:315px;top:71px">Timber is, in essence, a natural and warm material. Wood is also relatively durable and easy to work with, which has made it a favourite of builders throughout history. Our goal is to offer suitable products and quality furniture with installation and after-sales service to all of our clients. In order to achieve this, we're ready to help our clients in all stages of construction from design to production and maintenance.</p>
  <span class="abs read-more" style="left:315px;top:196px">Read More &nbsp;›</span>
</article>

<article class="abs service alt" style="top:1205px">
  <h3 class="abs serif" style="left:24px;top:22px">Stone Works</h3>
  <p class="abs" style="left:24px;top:71px">The natural stone found in the ground has been used in construction for centuries because of its durability. A structure built by a skilled craftsman from natural stone is unique, genuine and durable, and perfect for our bracing climate. Our experienced craftsmen are ready to help you in all stages of construction from planning to completion.</p>
  <span class="abs read-more" style="left:24px;top:196px">Read More &nbsp;›</span>
  <div class="abs service-img" style="left:598px;top:23px;background:linear-gradient(135deg,#8a7e70,#3d2e22)" role="img" aria-label="Photo of a stone fireplace with a lit fire">
    <span class="arrow" style="left:4px">‹</span><span class="arrow" style="right:4px">›</span>
    <span class="caption">Stone Fireplaces</span>
  </div>
</article>

<article class="abs service" style="top:1455px">
  <div class="abs service-img" style="left:21px;top:21px;background:linear-gradient(135deg,#a58566,#4a3424)" role="img" aria-label="Photo of a craftsman restoring an old wooden door">
    <span class="arrow" style="left:4px">‹</span><span class="arrow" style="right:4px">›</span>
    <span class="caption">Door Restoration</span>
  </div>
  <h3 class="abs serif" style="left:315px;top:20px">Restoration</h3>
  <p class="abs" style="left:315px;top:69px">It's good to see that fixing old things has become popular again in recent years and people are trying to find ways to preserve valuable old windows and pieces of furniture before deciding to open/replace them. It is possible to give a new life to almost any wooden door, window, piece of furniture or staircase. The extensive experience of our craftsmen will help you achieve the desired result.</p>
  <span class="abs read-more" style="left:315px;top:194px">Read More &nbsp;›</span>
</article>

<section class="about">
  <h2 class="abs section-title about-title serif" style="font-weight:400">About Us</h2>
  <div class="abs logo-box" style="left:169px;top:1847px;width:205px;height:111px">
    <svg viewBox="0 0 205 111" preserveAspectRatio="none"><line x1="0" y1="0" x2="205" y2="111" stroke="#555" stroke-width="1"/><line x1="205" y1="0" x2="0" y2="111" stroke="#555" stroke-width="1"/></svg>
    <span style="font-size:20px;bottom:12px">Quarnela</span>
  </div>
  <div class="abs about-text">
    <p>Quarnela is a company whose business operations include making wooden products, restoration and building structures from natural stone.</p>
    <p>All of our products are made by craftsmen and specialists who have extensive experience and knowledge in their fields.</p>
    <p>The products we offer are always handmade and we take the requests and ideas of the specific client into account We always strive to achieve the best possible quality.</p>
  </div>
</section>

<section class="contact">
  <div class="abs contact-photo" role="img" aria-label="Photo of a bright hallway with a stone wall and curved wooden staircase"></div>
  <div class="abs contact-panel"></div>
  <div class="abs contact-head">CONTACT &nbsp;PLEASE &nbsp;FILL IN THE FOLLOWING<br>FIELDS IF YOU WOULD LIKE A PRICE QUOTE</div>
  <div class="abs field" style="left:613px;top:2116px;width:203px;height:33px">Name*</div>
  <div class="abs field" style="left:825px;top:2116px;width:204px;height:33px">Phone*</div>
  <div class="abs field" style="left:613px;top:2154px;width:203px;height:35px">Email*</div>
  <div class="abs field" style="left:825px;top:2154px;width:204px;height:35px">Subject</div>
  <div class="abs field" style="left:613px;top:2196px;width:416px;height:94px">Message</div>
  <div class="abs btn btn-send">Get a Quote</div>
</section>

<footer class="abs footer">
  <div class="abs logo-box" style="left:183px;top:52px;width:88px;height:49px">
    <svg viewBox="0 0 88 49" preserveAspectRatio="none"><line x1="0" y1="0" x2="88" y2="49" stroke="#555" stroke-width="1"/><line x1="88" y1="0" x2="0" y2="49" stroke="#555" stroke-width="1"/></svg>
    <span style="font-size:9px;bottom:4px">Quarnela</span>
  </div>
  <div class="abs footer-info" style="left:184px;top:112px">
    <div>Telephone: +372 55 01234</div>
    <div>e-mail: hello@quarnela.ee</div>
    <div style="font-size:11px;margin-top:4px;letter-spacing:8px">f t</div>
  </div>
  <ul class="abs links" style="left:466px;top:46px"><li>About us</li><li>Services</li><li>Team</li><li>Gallery</li></ul>
  <ul class="abs links" style="left:615px;top:46px"><li>Support</li><li>FAQs</li><li>Warranty</li><li>Contact Us</li></ul>
  <h4 class="abs newsletter-title serif" style="left:766px;top:52px;font-weight:400">Get your newslwtter</h4>
  <div class="abs news-input">Your mail address...</div>
  <div class="abs btn btn-submit">SUBMIT</div>
  <div class="abs copyright">Copyright © Quarnela 2016</div>
  <div class="abs to-top"><svg width="34" height="34" viewBox="0 0 34 34"><path d="M11 20l6-6 6 6" fill="none" stroke="#fff" stroke-width="1.6"/></svg></div>
</footer>

</body>
</html>
```